Cutting Edge Cloud Hosting Provider needs business card design

We are a new Cloud Hosting Provider called Velkaro Hosting. (Velkaro means cloudy in Spanish.) We provide clients with virtual resources and not virtual machines directly. Our clients purchase the resources that they will use (RAM,CPU, Hard drive space) then use those resources in as many virtual machines as they like.

We are looking for a business card design that is cutting edge and hip.
Updates

The name of the company is "Velkaro Hosting". Please include the "Hosting" part of our name in the design.

Thanks

Target Market(s)

21-35 developers and I.T. Staff

Industry/Entity Type

Business

Requirements
Must have
• Rounded corners, Must Incorporate our logo, individual's name must be prominent

```html
<!DOCTYPE html>
<html lang="en">
<head>
<meta charset="utf-8">
<title>Velkaro Hosting – Business Card</title>
<link rel="stylesheet" href="https://fonts.googleapis.com/css2?family=Noto+Sans:wght@400;500&display=swap">
<style>
  :root {
    --backdrop: #f2f2f2;
    --card-top: #ffffff;
    --card-bottom: #e9eaec;
    --navy: #1b2a6b;
    --band-dark: #0b1a4a;
    --band-light: #1f3c8c;
    --card-shadow: rgba(0, 0, 0, 0.28);
  }
  * { margin: 0; padding: 0; box-sizing: border-box; }
  html, body {
    width: 1200px;
    height: 900px;
    overflow: hidden;
  }
  body {
    background: radial-gradient(ellipse at 50% 50%, #ffffff 0%, var(--backdrop) 70%, #e6e6e6 100%);
    font-family: "Noto Sans", Verdana, sans-serif;
    color: var(--navy);
    position: relative;
  }
  .card {
    position: absolute;
    top: 305px;
    width: 540px;
    height: 300px;
    border-radius: 18px;
    overflow: hidden;
    background: linear-gradient(180deg, var(--card-top) 0%, var(--card-bottom) 100%);
    box-shadow: 0 3px 8px var(--card-shadow);
  }
  .card--front { left: 45px; }
  .card--back { left: 615px; }
  .card__band {
    position: absolute;
    left: 0;
    right: 0;
    bottom: 0;
    height: 43px;
    background: linear-gradient(90deg, var(--band-dark) 0%, var(--band-light) 50%, var(--band-dark) 100%);
  }
  .wordmark {
    position: absolute;
    font-weight: 500;
    color: var(--navy);
    letter-spacing: 0.3px;
    line-height: 1;
    white-space: nowrap;
  }
  .card--front .wordmark {
    left: 25px;
    top: 66px;
    font-size: 27px;
  }
  .card--back .wordmark {
    left: 0;
    right: 0;
    top: 104px;
    text-align: center;
    font-size: 54px;
  }
  .person {
    position: absolute;
    left: 293px;
    top: 50px;
  }
  .person__name {
    font-size: 37px;
    font-weight: 400;
    line-height: 1.1;
    letter-spacing: 0.5px;
  }
  .person__title {
    font-size: 14px;
    margin-left: 7px;
    line-height: 1.1;
  }
  .contact {
    position: absolute;
    left: 340px;
    top: 180px;
    font-size: 14px;
    line-height: 20px;
    list-style: none;
  }
</style>
</head>
<body>
  <section class="card card--front" aria-label="Business card front">
    <div class="wordmark">velkaro hosting</div>
    <div class="person">
      <h1 class="person__name">Dario Lenz</h1>
      <p class="person__title">Vice-President</p>
    </div>
    <ul class="contact">
      <li>dario@velkaro.com</li>
      <li>call:- p. 210.555.0147</li>
      <li>call:- c. 210.555.0182</li>
    </ul>
    <div class="card__band"></div>
  </section>

  <section class="card card--back" aria-label="Business card back">
    <div class="wordmark">velkaro hosting</div>
    <div class="card__band"></div>
  </section>
</body>
</html>
```